Curl Radiant through and through. Hair stylist that specializes in extensions.

I am Marisol I am a hair stylist and I would like a website designed for my hair business.

I currently book clients via my profile on trimnook.example/marisolbrantley

I need a professional website ( curlradiantthroughandthrough.example ) to display photos and prices for services offered.

I would like to have a home page with a brief bio, Image with logo and testimonials at the bottom, and a header with tab that include: menu of services, gallery,and FAQs.

On the "Services" page, I'm not interested in photos on this page. Just the name of the service, brief description, and pricing. I would also like to have, on this page, "Appointment Request" with fields that include: Name, service requested, desired time frame (morning, afternoon, evening), and contact number and email

On the "Gallery" page, I would like pictures only, but arranged and/or presented in a creative way...

Target Market(s)

Women ages 25-55 who interested in hair extension services.

Industry/Entity Type

Hair And Beauty

Coding

Number of Pages Required

5+ page

Font styles to use
Sans Serif

Requirements
Must have
• Must include tabs that include, Menu of services offered, a quick fund link to pay deposits with ease, location, contact information, photo gallery, and policy/faqs.
Nice to have
• If possible i would like to stream music with the ability to be silenced. I would like a neutral color palette tans and beige.
Should not have
• stock images

```html
<!DOCTYPE html>
<html lang="en">
<head>
<meta charset="utf-8">
<title>Curl Radiant through and through</title>
<link href="https://fonts.googleapis.com/css2?family=Playfair+Display:ital,wght@0,400;1,400&family=Open+Sans:wght@400;600&display=swap" rel="stylesheet">
<style>
:root{
  --accent:#a87b52;
  --accent-dark:#8a6240;
  --espresso:#241b16;
  --ink:#2b231e;
  --muted:#7d7168;
  --white:#fff;
  --beige:#f4ede3;
  --sand:#e7d9c7;
  --line:#ddd2c4;
  --serif:'Playfair Display', Georgia, serif;
  --sans:'Open Sans', Arial, sans-serif;
}
*{box-sizing:border-box;margin:0;padding:0}
html,body{width:1200px;height:2695px;overflow:hidden}
body{position:relative;background:var(--white);font-family:var(--sans);color:var(--ink)}
.abs{position:absolute}

/* header + hero */
.hero{left:0;top:0;width:1200px;height:492px;background:linear-gradient(100deg,#cdbba5 0%,#b59b80 35%,#8c7058 55%,#b89f85 75%,#d3c3af 100%)}
.hero-shade{left:0;top:0;width:1200px;height:492px;background:linear-gradient(180deg,rgba(36,27,22,.05),rgba(36,27,22,.3))}
.topbar{left:0;top:0;width:1200px;height:77px;background:rgba(244,237,227,.25)}
.brand{left:105px;top:20px;font-family:var(--serif);font-size:30px;color:var(--white);display:flex;align-items:center;gap:10px}
.brand .dot{width:10px;height:10px;background:var(--accent)}
.nav{left:400px;top:28px;width:600px;display:flex;justify-content:space-between;font-family:var(--serif);font-style:italic;font-size:18px;color:var(--white)}
.search{left:1011px;top:0;width:84px;height:77px;background:var(--accent);color:var(--white);font-family:var(--serif);font-style:italic;font-size:14px;display:flex;align-items:center;justify-content:center;gap:6px}
.hero-kicker{left:0;top:232px;width:1200px;text-align:center;color:var(--white);font-size:20px}
.hero-title{left:0;top:268px;width:1200px;text-align:center;color:var(--white);font-family:var(--serif);font-style:italic;font-weight:400;font-size:44px;line-height:54px}
.btn-accent{background:var(--accent);color:var(--white);font-size:18px;display:flex;align-items:center;justify-content:center;border:2px solid var(--white)}
.hero-btn{left:529px;top:407px;width:142px;height:36px}
.arrow{top:272px}

/* section headings */
.sec-title{left:0;width:1200px;text-align:center;font-family:var(--serif);font-style:italic;font-weight:400;font-size:38px;color:var(--ink)}
.sec-rule{left:585px;width:30px;height:3px;background:var(--accent)}
.sec-thin{left:520px;width:160px;height:1px;background:var(--line)}

/* about */
.about-img{left:119px;top:615px;width:474px;height:290px;background:linear-gradient(160deg,#f1e7d9 0%,#cdb596 45%,#7a5638 100%)}
.about-copy{left:622px;top:608px;width:460px}
.about-copy h3{font-family:var(--serif);font-size:28px;font-weight:400;margin-bottom:8px}
.about-copy p{font-size:12.5px;line-height:18px;color:var(--muted);margin-bottom:16px}
.about-copy p.lead{font-style:italic}
.about-copy .tag{font-family:var(--serif);font-style:italic;font-size:15px;color:var(--ink)}
.btn-outline{border:2px solid var(--ink);color:var(--ink);font-size:17px;display:flex;align-items:center;justify-content:center;background:var(--white)}

/* promo cards */
.promo{top:1035px;height:209px;background:var(--espresso)}
.promo h4{position:absolute;left:24px;top:18px;font-family:var(--serif);font-size:26px;font-weight:400;color:var(--white)}
.promo p{position:absolute;left:24px;top:60px;width:226px;font-size:12.5px;line-height:19px;color:var(--sand)}
.promo .btn-dark{position:absolute;left:24px;top:160px;width:130px;height:32px;background:#4a3b31;color:var(--white);font-size:16px;display:flex;align-items:center;justify-content:center}
.promo-photo{top:1057px;width:200px;height:167px;border:6px solid var(--white);box-shadow:0 0 0 1px var(--line)}

/* services band */
.band{left:0;top:1306px;width:1200px;height:325px;background:linear-gradient(90deg,#2a1f19,#3a2c23 50%,#261c17)}
.band-title{color:var(--white)}
.service{top:1457px;width:202px;height:227px;border:5px solid var(--white);box-shadow:0 1px 4px rgba(0,0,0,.25)}
.service .fill{position:absolute;inset:0;background:linear-gradient(160deg,#faf5ee 0%,#efe3d3 60%,#e2cfb8 100%)}
.service h5{position:absolute;left:0;top:22px;width:100%;text-align:center;font-family:var(--serif);font-size:23px;font-weight:400;color:var(--accent-dark)}
.service .rule{position:absolute;left:86px;top:58px;width:20px;height:2px;background:var(--accent)}
.service svg{position:absolute;left:73px;top:80px}
.service .btn-outline{position:absolute;left:30px;top:164px;width:132px;height:34px;font-size:15px}

/* testimonials */
.quote-box{left:119px;top:1855px;width:976px;height:303px;border:1px solid var(--line);background:var(--white);box-shadow:0 0 6px rgba(0,0,0,.06)}
.quote-text{left:300px;top:1966px;width:600px;text-align:center;font-size:12.5px;line-height:20px;font-style:italic;color:#4a3f37}
.quote-name{left:0;top:2052px;width:1200px;text-align:center;font-family:var(--serif);font-size:26px}
.pager{top:2098px;width:24px;height:24px;border:1px solid var(--ink);display:flex;align-items:center;justify-content:center}

/* call to action */
.cta{left:0;top:2220px;width:1200px;height:169px;background:var(--espresso);border-top:5px solid var(--accent)}
.cta h2{position:absolute;left:0;top:26px;width:1200px;text-align:center;font-family:var(--serif);font-style:italic;font-weight:400;font-size:42px;color:var(--white)}
.cta .btn-accent{position:absolute;left:534px;top:102px;width:132px;height:34px;border:none;font-size:17px}

/* footer */
.footer{left:0;top:2389px;width:1200px;height:260px;background:linear-gradient(90deg,#1d1612,#33271f 50%,#1d1612)}
.f-col{top:2420px;color:#cbbba9;font-size:12.5px;line-height:22px}
.f-col h6{font-family:var(--serif);font-size:25px;font-weight:400;color:var(--white);margin-bottom:12px;line-height:32px}
.f-col b{color:var(--white);font-weight:400}
.f-thumb{width:70px;height:58px;background:linear-gradient(135deg,#e0d0bb,#8e7559);float:left;margin-right:12px;border:2px solid var(--sand)}
.deposit{display:inline-block;margin-top:12px;padding:2px 12px;background:var(--accent);color:var(--white);font-size:12px}
.grid{display:grid;grid-template-columns:repeat(3,54px);gap:4px}
.grid div{height:38px}
.bottom{left:0;top:2649px;width:1200px;height:46px;background:var(--espresso)}
.bottom .brand{left:119px;top:8px;font-size:22px}
.bottom .copy{position:absolute;right:105px;top:14px;color:var(--white);font-size:13px}
</style>
</head>
<body>

<!-- header + hero -->
<div class="abs hero" role="img" aria-label="Photo of Marisol with long flowing extensions in the studio"></div>
<div class="abs hero-shade"></div>
<div class="abs topbar"></div>
<div class="abs brand"><span>Curl Radiant</span><span class="dot"></span></div>
<nav class="abs nav">
  <span>Home</span><span>Services</span><span>Gallery</span><span>FAQs</span><span>Deposit</span><span>Location</span><span>Contact</span>
</nav>
<div class="abs search">
  <svg width="12" height="12" viewBox="0 0 12 12"><circle cx="5" cy="5" r="3.6" fill="none" stroke="#fff" stroke-width="1.6"/><line x1="7.6" y1="7.6" x2="11" y2="11" stroke="#fff" stroke-width="1.8"/></svg>
  Search
</div>
<svg class="abs arrow" style="left:100px" width="40" height="44" viewBox="0 0 40 44"><polygon points="36,2 4,22 36,42 28,22" fill="#6e5a4a" opacity=".85"/></svg>
<svg class="abs arrow" style="left:1056px" width="40" height="44" viewBox="0 0 40 44"><polygon points="4,2 36,22 4,42 12,22" fill="#6e5a4a" opacity=".85"/></svg>
<div class="abs hero-kicker">Extensions that blend with your natural texture</div>
<h1 class="abs hero-title">Length, Volume and Confidence<br>Made to Match You</h1>
<div class="abs btn-accent hero-btn">View Services</div>

<!-- about -->
<h2 class="abs sec-title" style="top:520px">About Marisol</h2>
<div class="abs sec-thin" style="top:577px"></div>
<div class="abs sec-rule" style="top:576px"></div>
<div class="abs about-img" role="img" aria-label="Photo of the Curl Radiant studio with styling chair and mirror"></div>
<div class="abs about-copy">
  <h3>Extensions, done with care</h3>
  <p>I am Marisol, an extension specialist who blends custom hair with your natural texture so the result feels light, moves freely and lasts for weeks with simple care at home. Every visit starts with a talk about your routine.</p>
  <p class="lead">My studio is calm and private, stocked with quality hair I trust. Book a consultation and we will plan colour, length and volume together before a single strand is placed.</p>
  <div class="tag">Curl Radiant through and through</div>
</div>
<div class="abs btn-outline" style="left:622px;top:870px;width:136px;height:34px">Read More</div>

<!-- promotions -->
<h2 class="abs sec-title" style="top:942px">Our Promotions</h2>
<div class="abs sec-thin" style="top:999px"></div>
<div class="abs sec-rule" style="top:998px"></div>

<div class="abs promo" style="left:119px;width:336px">
  <h4>Only Until March</h4>
  <p>Book a full sew-in before the end of March and enjoy a free silk press and care kit.</p>
  <div class="btn-dark">Book Now</div>
</div>
<div class="abs promo-photo" style="left:391px;background:linear-gradient(150deg,#e6c79c,#b98a5a 60%,#7d5634)" role="img" aria-label="Client with long honey-toned wavy extensions"></div>

<div class="abs promo" style="left:620px;width:336px">
  <h4>New Clients</h4>
  <p>Enjoy fifteen percent off tape-in extensions this month, plus a follow-up trim.</p>
  <div class="btn-dark">Book Now</div>
</div>
<div class="abs promo-photo" style="left:885px;background:linear-gradient(150deg,#f3ece2,#9a8370 55%,#2b211b)" role="img" aria-label="Client with a sleek dark bob"></div>

<!-- services band -->
<div class="abs band" role="img" aria-label="Dark warm background of styled hair"></div>
<h2 class="abs sec-title band-title" style="top:1330px">Menu of Services</h2>
<div class="abs sec-rule" style="top:1386px"></div>

<div class="abs service" style="left:119px">
  <div class="fill"></div>
  <h5>Sew-In Install</h5><div class="rule"></div>
  <svg width="46" height="56" viewBox="0 0 46 56"><circle cx="12" cy="46" r="7" fill="none" stroke="#2b231e" stroke-width="3"/><circle cx="34" cy="46" r="7" fill="none" stroke="#2b231e" stroke-width="3"/><line x1="16" y1="40" x2="34" y2="4" stroke="#2b231e" stroke-width="4"/><line x1="30" y1="40" x2="12" y2="4" stroke="#2b231e" stroke-width="4"/></svg>
  <div class="btn-outline">View Prices</div>
</div>
<div class="abs service" style="left:378px">
  <div class="fill"></div>
  <h5>Tape-Ins</h5><div class="rule"></div>
  <svg width="46" height="56" viewBox="0 0 46 56"><rect x="6" y="6" width="34" height="10" rx="2" fill="#2b231e"/><g fill="#2b231e"><rect x="9" y="16" width="3" height="34"/><rect x="16" y="16" width="3" height="34"/><rect x="23" y="16" width="3" height="34"/><rect x="30" y="16" width="3" height="34"/><rect x="36" y="16" width="3" height="34"/></g></svg>
  <div class="btn-outline">View Prices</div>
</div>
<div class="abs service" style="left:635px">
  <div class="fill"></div>
  <h5>Clip-Ins</h5><div class="rule"></div>
  <svg width="46" height="56" viewBox="0 0 46 56"><rect x="8" y="14" width="30" height="28" rx="4" fill="none" stroke="#2b231e" stroke-width="4"/><rect x="16" y="22" width="14" height="12" fill="#2b231e"/></svg>
  <div class="btn-outline">View Prices</div>
</div>
<div class="abs service" style="left:888px">
  <div class="fill"></div>
  <h5>Color Match</h5><div class="rule"></div>
  <svg width="46" height="56" viewBox="0 0 46 56"><path d="M23 4 C23 4 8 24 8 36 a15 15 0 0 0 30 0 C38 24 23 4 23 4z" fill="#2b231e"/></svg>
  <div class="btn-outline">View Prices</div>
</div>

<!-- testimonials -->
<h2 class="abs sec-title" style="top:1748px">What Customers Say</h2>
<div class="abs sec-thin" style="top:1805px"></div>
<div class="abs sec-rule" style="top:1804px"></div>

<div class="abs" style="left:0;top:1750px;width:90px;height:130px;background:linear-gradient(150deg,#c9a27c,#8a6240)" role="img" aria-label="Tan powder decoration"></div>
<div class="abs" style="left:0;top:1895px;width:80px;height:110px;background:radial-gradient(circle at 35% 45%,#dcc0a0,#b8916b 60%,rgba(255,255,255,0) 72%)" role="img" aria-label="Loose beige powder decoration"></div>
<div class="abs" style="left:60px;top:2050px;width:70px;height:70px;background:radial-gradient(circle,#c9a886,#a07a58 55%,rgba(255,255,255,0) 72%)" role="img" aria-label="Bronzer swatch decoration"></div>
<div class="abs" style="left:1040px;top:1740px;width:140px;height:110px;background:radial-gradient(circle at 50% 50%,#e8d3bb,#c9a989 55%,rgba(255,255,255,0) 72%)" role="img" aria-label="Sand powder decoration"></div>
<div class="abs" style="left:1100px;top:1890px;width:90px;height:100px;background:linear-gradient(160deg,#6b5747,#241b16)" role="img" aria-label="Brush decoration"></div>
<div class="abs" style="left:1040px;top:2020px;width:140px;height:110px;background:radial-gradient(circle at 55% 50%,#b08a62,#7d5a3a 55%,rgba(255,255,255,0) 72%)" role="img" aria-label="Caramel powder decoration"></div>

<div class="abs quote-box"></div>
<svg class="abs" style="left:572px;top:1889px" width="56" height="56" viewBox="0 0 56 56"><circle cx="28" cy="28" r="28" fill="#a87b52"/><path d="M18 22h8v8c0 5-3 8-7 9l-1-3c2-1 3-3 3-5h-3zM31 22h8v8c0 5-3 8-7 9l-1-3c2-1 3-3 3-5h-3z" fill="#fff"/></svg>
<p class="abs quote-text">Marisol listened to every detail and matched my extensions so well that nobody could tell where my own hair ended. The install felt light from day one and still looks fresh after six weeks. The studio is relaxing, the booking was easy and I will never go anywhere else.</p>
<div class="abs quote-name">“Delia Marsh”</div>
<div class="abs pager" style="left:576px"><svg width="8" height="10" viewBox="0 0 8 10"><polyline points="6,1 2,5 6,9" fill="none" stroke="#2b231e" stroke-width="1.6"/></svg></div>
<div class="abs pager" style="left:604px"><svg width="8" height="10" viewBox="0 0 8 10"><polyline points="2,1 6,5 2,9" fill="none" stroke="#2b231e" stroke-width="1.6"/></svg></div>

<!-- call to action -->
<section class="abs cta">
  <h2>Book Your Next Appointment Today!</h2>
  <div class="btn-accent">Book Now</div>
</section>

<!-- footer -->
<div class="abs footer" role="img" aria-label="Dark warm photo of styling tools"></div>
<div class="abs f-col" style="left:119px;width:250px">
  <h6>About Us</h6>
  <div class="f-thumb" role="img" aria-label="Small photo of the studio"></div>
  <p style="font-style:italic">A calm studio for extensions and care, led by Marisol with years of hands-on craft.</p>
</div>
<div class="abs f-col" style="left:407px;width:240px;font-size:12px">
  <h6>Contact us on</h6>
  <div>Phone: <b>+1 555 014 2290</b></div>
  <div>Location: <b>214 Linden Ave, Suite 3</b></div>
  <div><b>curlradiantthroughandthrough.example</b></div>
  <div class="deposit">Pay deposit with quick fund</div>
</div>
<div class="abs f-col" style="left:660px;width:230px">
  <h6>Opening Time</h6>
  <div>Monday-Friday: ........ 8.00 to 18.00</div>
  <div>Saturday: ........ 9.00 to 16.00</div>
  <div>Sunday: ........ closed</div>
  <div>Policies and FAQs are listed on the FAQs page.</div>
</div>
<div class="abs f-col" style="left:925px;width:180px">
  <h6>Our gallery</h6>
  <div class="grid" role="img" aria-label="Thumbnail gallery of finished extension styles">
    <div style="background:#c9a27c"></div><div style="background:#8a6240"></div><div style="background:#e3cfb6"></div>
    <div style="background:#6e4f36"></div><div style="background:#d8bc9a"></div><div style="background:#4a3628"></div>
    <div style="background:#b48a63"></div><div style="background:#efe1cd"></div><div style="background:#3a2c23"></div>
  </div>
</div>
<div class="abs bottom">
  <div class="abs brand"><span>Curl Radiant</span></div>
  <div class="copy">© 2016 - Curl Radiant. All Rights Reserved</div>
</div>

</body>
</html>
```